We want a business card/punch card for our business. We are including examples of our current business card (we like the front of our business card and not looking to remake it). We need only back side to be designed in form of a punch card (we are including a sample of the punch card we made, but are unsatisfied). For each $180 spend (9 punches) our clients have $20 off.

Colors
886aae

```html
<!DOCTYPE html>
<html lang="en">
<head>
<meta charset="utf-8">
<title>Lunar Path Studio – Appreciation Punch Card</title>
<link rel="stylesheet" href="https://fonts.googleapis.com/css2?family=Gelasio:ital,wght@0,400;0,700;1,400&display=swap">
<style>
  :root {
    --stage: #2a2c30;
    --purple-deep: #4a1d93;
    --purple-mid: #6a30b8;
    --purple-glow: #8a44c9;
    --lavender: #886aae;
    --periwinkle: #6e6ccf;
    --ink: #1d1b22;
    --white: #ffffff;
  }
  * { box-sizing: border-box; margin: 0; padding: 0; }
  html, body { width: 1200px; height: 900px; overflow: hidden; }
  body {
    background: var(--stage);
    font-family: "Gelasio", Georgia, serif;
    position: relative;
  }
  .card {
    position: absolute;
    width: 540px;
    height: 310px;
    border-radius: 22px;
    overflow: hidden;
    box-shadow: 0 14px 30px rgba(0,0,0,.45);
  }

  /* Punch card (back) */
  .punch-card { left: 40px; top: 295px; background: var(--purple-mid); }
  .punch-card__pattern {
    position: absolute; inset: 0;
    background: radial-gradient(ellipse at 45% 45%, var(--purple-glow) 0%, var(--purple-mid) 45%, var(--purple-deep) 100%);
  }
  .punch-card__art { position: absolute; inset: 0; }
  .punch-card__title {
    position: absolute; left: 0; right: 0; top: 112px;
    text-align: center; color: var(--white);
    font-weight: 700; font-size: 35px; letter-spacing: .3px;
  }
  .punch-card__terms {
    position: absolute; left: 0; right: 0; top: 162px;
    text-align: center; color: var(--white);
    font-size: 15px;
  }
  .punch-badge__label {
    font-family: "Gelasio", Georgia, serif;
    font-weight: 700; font-size: 14px; fill: var(--purple-mid);
  }

  /* Front card */
  .front-card { left: 620px; top: 295px; background: var(--white); }
  .front-card__waves { position: absolute; inset: 0; }
  .front-card__brand {
    position: absolute; left: 28px; top: 52px;
    display: flex; align-items: center; gap: 10px;
    color: var(--purple-mid); font-size: 30px; font-weight: 700;
    line-height: 1;
  }
  .front-card__brand-dot {
    width: 16px; height: 16px; border-radius: 50%;
    background: var(--lavender);
  }
  .front-card__message {
    position: absolute; right: 26px; top: 30px; width: 280px;
    font-style: italic; font-size: 14px; line-height: 1.3;
    color: var(--ink); text-align: right;
  }
  .front-card__web {
    position: absolute; right: 26px; top: 200px;
    color: var(--purple-mid); font-size: 21px;
  }
</style>
</head>
<body>

  <section class="card punch-card" aria-label="Lunar Appreciation punch card">
    <div class="punch-card__pattern" role="img" aria-label="Faint mandala pattern on purple background"></div>
    <svg class="punch-card__art" width="540" height="310" viewBox="0 0 540 310" aria-hidden="true">
      <defs>
        <polygon id="starburst" fill="#ffffff"
          points="26,0 19.3,5.2 22.5,13 14.1,14.1 13,22.5 5.2,19.3 0,26 -5.2,19.3 -13,22.5 -14.1,14.1 -22.5,13 -19.3,5.2 -26,0 -19.3,-5.2 -22.5,-13 -14.1,-14.1 -13,-22.5 -5.2,-19.3 0,-26 5.2,-19.3 13,-22.5 14.1,-14.1 22.5,-13 19.3,-5.2"/>
      </defs>
      <g class="punch-row punch-row--top">
        <g transform="translate(70 45)"><use href="#starburst"/><text class="punch-badge__label" text-anchor="middle" y="5">$20</text></g>
        <g transform="translate(170 45)"><use href="#starburst"/><text class="punch-badge__label" text-anchor="middle" y="5">$20</text></g>
        <g transform="translate(270 45)"><use href="#starburst"/><text class="punch-badge__label" text-anchor="middle" y="5">$20</text></g>
        <g transform="translate(370 45)"><use href="#starburst"/><text class="punch-badge__label" text-anchor="middle" y="5">$20</text></g>
        <g transform="translate(470 45)"><use href="#starburst"/><text class="punch-badge__label" text-anchor="middle" y="5">$20</text></g>
      </g>
      <g class="punch-row punch-row--bottom">
        <g transform="translate(70 262)"><use href="#starburst"/><text class="punch-badge__label" text-anchor="middle" y="5">$20</text></g>
        <g transform="translate(170 262)"><use href="#starburst"/><text class="punch-badge__label" text-anchor="middle" y="5">$20</text></g>
        <g transform="translate(270 262)"><use href="#starburst"/><text class="punch-badge__label" text-anchor="middle" y="5">$20</text></g>
        <g transform="translate(370 262)"><use href="#starburst"/><text class="punch-badge__label" text-anchor="middle" y="5">$20</text></g>
        <g transform="translate(470 262)"><use href="#starburst"/><text class="punch-badge__label" text-anchor="middle" y="5">$20</text></g>
      </g>
    </svg>
    <h1 class="punch-card__title">Lunar Appreciation Card</h1>
    <p class="punch-card__terms">For each $180 spend (9 punches) our clients have $20 off.</p>
  </section>

  <section class="card front-card" aria-label="Lunar Path Studio front card">
    <svg class="front-card__waves" width="540" height="310" viewBox="0 0 540 310" aria-hidden="true">
      <defs>
        <linearGradient id="waveFill" x1="0" y1="0" x2="1" y2="1">
          <stop offset="0" stop-color="#5b2aa6"/>
          <stop offset="1" stop-color="#7a3cc0"/>
        </linearGradient>
      </defs>
      <path d="M0 150 C110 150 200 200 290 260 C330 285 360 300 380 310 L0 310 Z" fill="var(--periwinkle)"/>
      <path d="M0 165 C60 160 120 175 170 205 C150 190 90 172 0 178 Z" fill="#ffffff"/>
      <path d="M0 185 C120 180 210 230 280 280 C300 295 318 305 330 310 L0 310 Z" fill="url(#waveFill)"/>
      <path d="M0 240 C90 235 160 260 220 310 L0 310 Z" fill="#6a30b8" opacity=".6"/>
    </svg>
    <div class="front-card__brand">
      <span class="front-card__brand-dot"></span>
      <span class="front-card__brand-name">Lunar Path</span>
    </div>
    <p class="front-card__message">This card is a symbol of appreciation from us to you, without your business we would not be able to do what we love most. When you fill out this card you will receive $20 toward your next Weekly Event, Workshop or Private Session.</p>
    <p class="front-card__web">www.LunarPathStudio.com</p>
  </section>

</body>
</html>
```